Professional violinist needs business cards

I am trying to attract the following jobs:
-private violin lessons (primarily classical)
-performance gigs (weddings, birthday parties, funerals, etc.)
-collaborations with other artists (studio recordings, performances)

I want to communicate that I have a very high standard of excellence for my work, but I also love people and celebrations.
Values/style words I like are:
love, joy, peace, fun, beauty, authenticity, excellence, warmth, refined/sleek, free spirited. If that's too confusing, just ignore :)

I will attach my favorite business card template that I could find on Canva. The lines are supposed to be like a music staff, which I think is really cool, but I also don't want it to look too busy. I like the simple black and white--I think it looks sharp--but I also am open to other ideas. I also have seen business cards with pictures included that looked great, so I attached an image that could be used as well.

I am also attaching a file that I made of my initials that could be used as a logo, but I'm not sure if it should be included.

Information on the card:
-My name (18 letters total)
-"violinist"
-phone number, email, website

Thank you!

```html
<!DOCTYPE html>
<html lang="en">
<head>
<meta charset="UTF-8">
<title>Elena Marlowe – Violinist Business Card</title>
<link rel="stylesheet" href="https://fonts.googleapis.com/css2?family=Open+Sans:wght@400;700&family=Noto+Sans:wght@400;700&display=swap">
<style>
  :root {
    --page-bg: #3a3a3b;
    --card-bg: #c9bcae;
    --card-bg-light: #d3c8bb;
    --card-bg-dark: #b3a595;
    --ink: #2c2b2a;
    --ink-soft: #3d3b39;
    --photo-wall: #6d655b;
    --photo-dress: #1c1a19;
  }
  * { margin: 0; padding: 0; box-sizing: border-box; }
  html, body {
    width: 1200px;
    height: 900px;
    overflow: hidden;
    background: var(--page-bg);
  }
  .sheet {
    position: relative;
    width: 1200px;
    height: 900px;
  }
  .card {
    position: absolute;
    left: 240px;
    width: 720px;
    height: 410px;
    border-radius: 38px;
    overflow: hidden;
    background: var(--card-bg);
    box-shadow: 0 10px 24px rgba(0,0,0,0.35);
  }
  .card--back { top: 35px; }
  .card--front { top: 465px; }

  .soundhole-art {
    position: absolute;
    inset: 0;
    background:
      radial-gradient(circle at 68% 55%, var(--card-bg-dark) 0 120px, transparent 122px),
      radial-gradient(circle at 68% 55%, var(--card-bg-light) 0 175px, transparent 177px),
      linear-gradient(160deg, var(--card-bg-light), var(--card-bg));
    opacity: 0.85;
  }

  /* back side */
  .brand-name {
    position: absolute;
    top: 58px;
    right: 70px;
    font-family: "Open Sans", sans-serif;
    font-weight: 700;
    font-size: 34px;
    color: var(--ink);
  }
  .services {
    position: absolute;
    left: 60px;
    bottom: 60px;
    list-style: none;
    font-family: "Open Sans", sans-serif;
    color: var(--ink);
  }
  .service { margin-top: 16px; }
  .service__title {
    display: block;
    font-weight: 700;
    font-size: 22px;
    line-height: 1.15;
  }
  .service__detail {
    display: block;
    font-size: 18px;
    color: var(--ink-soft);
    line-height: 1.2;
  }

  /* front side */
  .portrait {
    position: absolute;
    left: 0;
    bottom: 0;
    width: 330px;
    height: 300px;
    background:
      linear-gradient(90deg, transparent 0 38%, var(--photo-dress) 38% 78%, transparent 78%),
      linear-gradient(135deg, var(--photo-wall), #8a8174);
  }
  .contact {
    position: absolute;
    left: 380px;
    top: 120px;
    font-family: "Noto Sans", sans-serif;
    color: var(--ink);
  }
  .contact__name {
    font-weight: 700;
    font-size: 30px;
    line-height: 1.1;
  }
  .contact__role {
    font-size: 22px;
    margin-bottom: 12px;
  }
  .contact__list { list-style: none; }
  .contact__item {
    display: flex;
    align-items: center;
    gap: 10px;
    font-size: 20px;
    line-height: 1.45;
  }
  .contact__icon { width: 22px; height: 22px; flex: none; }
</style>
</head>
<body>
<main class="sheet">

  <section class="card card--back" aria-label="Card back">
    <div class="soundhole-art" role="img" aria-label="Faint photograph of a guitar soundhole and strings"></div>
    <div class="brand-name">Elena Marlowe</div>
    <ul class="services">
      <li class="service">
        <span class="service__title">Private violin lessons</span>
        <span class="service__detail">(primarily classical)</span>
      </li>
      <li class="service">
        <span class="service__title">Performance gigs</span>
        <span class="service__detail">(weddings, birthday parties, funerals, etc.)</span>
      </li>
      <li class="service">
        <span class="service__title">Collaborations with other artists</span>
        <span class="service__detail">(studio recordings, performances)</span>
      </li>
    </ul>
  </section>

  <section class="card card--front" aria-label="Card front">
    <div class="soundhole-art" role="img" aria-label="Faint photograph of a guitar soundhole and strings"></div>
    <div class="portrait" role="img" aria-label="Photograph of the violinist in a black dress holding a violin by a stone wall"></div>
    <div class="contact">
      <h1 class="contact__name">Elena Marlowe</h1>
      <p class="contact__role">Violinist</p>
      <ul class="contact__list">
        <li class="contact__item">
          <svg class="contact__icon" viewBox="0 0 24 24" aria-hidden="true">
            <rect x="1.5" y="1.5" width="21" height="21" rx="4" fill="none" stroke="currentColor" stroke-width="2"/>
            <path d="M8 6c-1 1-1.5 2 0 5s4 5 6 6c1.5.6 2.5 0 3.5-1l-2-2-1.5 1c-1-.5-3-2.5-3.5-3.5l1-1.5z" fill="currentColor"/>
          </svg>
          055-987 321 640
        </li>
        <li class="contact__item">
          <svg class="contact__icon" viewBox="0 0 24 24" aria-hidden="true">
            <rect x="1" y="5" width="22" height="14" fill="currentColor"/>
            <path d="M1 5l11 8 11-8" fill="none" stroke="var(--card-bg)" stroke-width="1.6"/>
          </svg>
          hello@elenamarlowe.net
        </li>
        <li class="contact__item">
          <svg class="contact__icon" viewBox="0 0 24 24" aria-hidden="true">
            <circle cx="12" cy="12" r="11" fill="currentColor"/>
            <g fill="none" stroke="var(--card-bg)" stroke-width="1.3">
              <ellipse cx="12" cy="12" rx="4.5" ry="11"/>
              <path d="M1 12h22M3 6.5h18M3 17.5h18M12 1v22"/>
            </g>
          </svg>
          www.elenamarlowe.net
        </li>
      </ul>
    </div>
  </section>

</main>
</body>
</html>
```